Church Lanterns Over Millbrook Gospel Booklet Design

We need a booklet designed that we will be printing to hand out in our community. Wording for each page will be provided and we need graphic design to produce the layouts in a format ready for print. Booklet will be 4.75" x 4.75" square and a total of 12 pages: 1 cover page front, 1 cover page back, 10 inside pages some of which will be full spread across 2 pages.

Target Market(s)

English speaking Westerners

Industry/Entity Type

Religious

Font styles to use
Serif

Colors
ffffff
85abd2
0292cd
33b8a4
5c5c5c

Requirements
Must have
• Minimalist design with clean look described in attached document
Nice to have
• Aesthetically pleasing graphics, crisp fonts, excellent turn around times
Should not have
• Effeminate design, busy look with too much graphic and text

```html
<!DOCTYPE html>
<html lang="en">
<head>
<meta charset="utf-8">
<title>Gospel Booklet – Spread and Cover</title>
<link href="https://fonts.googleapis.com/css2?family=Crimson+Text:ital,wght@0,400;0,600;0,700;1,400;1,600&display=swap" rel="stylesheet">
<style>
  :root{
    --white:#ffffff;
    --sky:#85abd2;
    --blue:#0292cd;
    --teal:#33b8a4;
    --slate:#5c5c5c;
    --ink:#3d3d3d;
    --stage:#e6e6e6;
  }
  *{box-sizing:border-box;margin:0;padding:0}
  html,body{width:1200px;height:1200px;overflow:hidden}
  body{background:var(--stage);font-family:"Crimson Text",serif;color:var(--ink);position:relative}

  .spread{position:absolute;left:80px;top:40px;width:1040px;height:520px;display:flex;box-shadow:0 6px 18px rgba(0,0,0,.18)}
  .page{position:relative;width:520px;height:520px;background:var(--white);overflow:hidden}
  .page--left{background:linear-gradient(to left,#e4e4e4 0,#fff 60px)}
  .page--right{background:linear-gradient(to right,#ececec 0,#fff 40px)}

  .intro{position:absolute;left:50px;top:52px;width:420px;font-size:19px;line-height:1.3}
  .truths{position:absolute;left:50px;top:122px;width:430px;list-style:none}
  .truth{display:flex;gap:12px;align-items:flex-start;padding:10px 0 12px;border-bottom:1px solid var(--slate)}
  .truth:last-child{border-bottom:none}
  .truth__marker{display:flex;align-items:center;gap:3px;flex:none;margin-top:4px}
  .truth__step{width:13px;height:17px;background:var(--c)}
  .truth__step:nth-child(1){opacity:.25}
  .truth__step:nth-child(2){opacity:.5}
  .truth__step:nth-child(3){opacity:.75}
  .truth__num{width:30px;height:20px;background:var(--c);color:var(--white);font-size:14px;font-style:italic;text-align:center;line-height:20px}
  .truth__text{font-style:italic;font-size:18px;line-height:1.25}
  .truth--1{--c:var(--sky)} .truth--2{--c:var(--blue)} .truth--3{--c:var(--teal)} .truth--4{--c:var(--slate)}

  .folio{position:absolute;bottom:30px;height:34px;width:100%}
  .folio__rule{position:absolute;bottom:0;height:2px;background:var(--sky)}
  .folio__band{position:absolute;bottom:6px;height:12px;width:190px;background:var(--blue)}
  .folio__label{position:absolute;bottom:20px;font-size:13px;letter-spacing:.02em;text-transform:uppercase;color:var(--slate);white-space:nowrap}
  .page--left .folio__rule{left:40px;width:300px}
  .page--left .folio__band{right:0}
  .page--left .folio__label{right:24px}
  .page--right .folio__rule{right:40px;width:300px}
  .page--right .folio__band{left:0}
  .page--right .folio__label{left:24px}

  .body-copy{position:absolute;left:60px;top:60px;width:400px;font-size:19px;line-height:1.3}
  .verse-ref{position:absolute;left:60px;top:230px;background:var(--blue);color:var(--white);font-size:14px;padding:2px 12px 2px 100px;letter-spacing:.03em}
  .verse{position:absolute;left:110px;top:258px;font-style:italic;font-size:30px;color:var(--slate);white-space:nowrap}
  .statue{position:absolute;right:64px;top:306px;width:180px;height:140px;background:linear-gradient(135deg,#7d8f89,#3a4442 60%,#2a302f)}
  .statue__bar{position:absolute;right:40px;top:296px;width:14px;height:130px;background:var(--sky)}

  .cover{position:absolute;left:340px;top:620px;width:520px;height:520px;display:flex;box-shadow:0 6px 18px rgba(0,0,0,.2)}
  .cover__spine{width:62px;height:100%;background:linear-gradient(to right,#6f9bc8,var(--sky) 70%,#a4c2e0)}
  .cover__photo{flex:1;position:relative;background:linear-gradient(to bottom,#c9a79a 0%,#e8b87a 22%,#c98f63 38%,#8a8f86 48%,#4f6b3b 60%,#2f4a22 80%,#243a1a 100%)}
  .cover__title{position:absolute;left:50px;top:120px;width:380px;font-weight:700;line-height:1;color:var(--blue)}
  .cover__line{display:block}
  .cover__line--small{font-size:40px}
  .cover__line--large{font-size:76px}
</style>
</head>
<body>

<section class="spread" aria-label="Inside spread">
  <article class="page page--left">
    <p class="intro">This story establishes some foundational truths about all of us:</p>
    <ol class="truths">
      <li class="truth truth--1">
        <span class="truth__marker"><span class="truth__step"></span><span class="truth__step"></span><span class="truth__step"></span><span class="truth__num">1.</span></span>
        <span class="truth__text">God loves us - he didn't have to create us; we are here because he couldn't imagine life without us.</span>
      </li>
      <li class="truth truth--2">
        <span class="truth__marker"><span class="truth__step"></span><span class="truth__step"></span><span class="truth__step"></span><span class="truth__num">2.</span></span>
        <span class="truth__text">God is the proper authority in our lives - if he designed and made us, he rightfully owns us.</span>
      </li>
      <li class="truth truth--3">
        <span class="truth__marker"><span class="truth__step"></span><span class="truth__step"></span><span class="truth__step"></span><span class="truth__num">3.</span></span>
        <span class="truth__text">God knows the purpose of our lives - if he designed and made us, he knows why we are here.</span>
      </li>
      <li class="truth truth--4">
        <span class="truth__marker"><span class="truth__step"></span><span class="truth__step"></span><span class="truth__step"></span><span class="truth__num">4.</span></span>
        <span class="truth__text">God's truth is the truth we need - if he designed and made us, he knows what it takes for life to go well for us.</span>
      </li>
    </ol>
    <footer class="folio"><span class="folio__rule"></span><span class="folio__label">Lanterns Over Millbrook</span><span class="folio__band"></span></footer>
  </article>

  <article class="page page--right">
    <p class="body-copy">But we, mankind, have all rejected God's authority in our lives. And because he rightfully owns us, our rebellion against God is a grave injustice; an act of treason for which we deserve to be cut off from God forever.</p>
    <span class="verse-ref">ROMANS 6:23</span>
    <p class="verse">“For the wages of sin is death...”</p>
    <span class="statue__bar"></span>
    <div class="statue" role="img" aria-label="Photo of a bronze statue hand holding a wilted rose"></div>
    <footer class="folio"><span class="folio__rule"></span><span class="folio__label">Lanterns Over Millbrook</span><span class="folio__band"></span></footer>
  </article>
</section>

<section class="cover" aria-label="Front cover">
  <div class="cover__spine"></div>
  <div class="cover__photo" role="img" aria-label="Photo of a forested mountain valley under a golden sunset sky">
    <h1 class="cover__title">
      <span class="cover__line cover__line--small">The</span>
      <span class="cover__line cover__line--large">Gospel</span>
      <span class="cover__line cover__line--small">of</span>
      <span class="cover__line cover__line--large">Jesus Christ</span>
    </h1>
  </div>
</section>

</body>
</html>
```